Brightwave HR - DL Postcard Fliers

I have a need to get some quotes to create a series of postcard fliers to promote my Human Resources Consultancy & Contracting services. I'd like to start with one to get a feel for how they might look when I introduce other products/services connected to my business. I think DL size would work best (99 x 210 mm). I have enclosed an A4 sheet that has a LOT of content. Would like it to be more visual and less wordy. Id like to feature my broader HR services on back side and the specific product/service offering on the front. For the first one, I would like the focus to be on recruitment. Perhaps need to highlight 20% off as an introductory rate off already cost effective flat rate structure for recruitment. Please keep punchy, less wordy. Happy to review some options you may done for someone else in the past and work with you on final content. Good luck.
Updates

Hi All. I am about 5 days away from making a decision now. I posted a request for an updated logo design last week and am waiting on submissions. Once i have decided on logo design, I will ask you to incorporate into your designs. It will have same coloring and not be too different so should be able to quickly incorporate into your designs. Thanks for your patience.

Target Market(s)

Small to medium enterprises

Industry/Entity Type

Quotes

Font styles to use
Serif

Colors
ec1f27

Requirements
Must have
• Contact Details - mobile, website, email
• Specifics on what product offering is and benefits
• A Call to action
• Ideally double sided DL - landscape view - one side with general information about the business generally, the other side with a specific focus on one product/service offering from within my business.
Should not have
• Too many words.

```html
<!DOCTYPE html>
<html lang="en">
<head>
<meta charset="utf-8">
<title>Brightwave HR – Recruitment Special Postcard</title>
<link href="https://fonts.googleapis.com/css2?family=Arimo:wght@400;700&family=Tinos:wght@400;700&display=swap" rel="stylesheet">
<style>
  :root {
    --brand-red: #ec1f27;
    --ink: #111111;
    --paper: #ffffff;
    --backdrop: #e6e6e6;
    --photo-light: #e9ebee;
    --photo-mid: #b9c0c8;
    --photo-dark: #4a5160;
  }
  * { box-sizing: border-box; margin: 0; padding: 0; }
  html, body { width: 1200px; height: 900px; overflow: hidden; }
  body { position: relative; background: var(--backdrop); font-family: "Arimo", Arial, sans-serif; color: var(--ink); }

  .postcard { position: absolute; left: 212px; width: 769px; height: 383px; background: var(--paper); overflow: hidden; box-shadow: 0 2px 6px rgba(0,0,0,.18); }
  .postcard--front { top: 57px; }
  .postcard--back { top: 463px; }

  .front-art { position: absolute; inset: 0; }

  .brand-name { position: absolute; font-family: "Arimo", Arial, sans-serif; font-weight: 400; font-size: 25px; color: var(--brand-red); white-space: nowrap; line-height: 1; }
  .postcard--front .brand-name { right: 23px; top: 22px; }
  .postcard--back .brand-name { right: 42px; top: 320px; }

  .discount-badge { position: absolute; left: 170px; top: 232px; width: 112px; height: 112px; border-radius: 50%; background: var(--brand-red); color: var(--paper); display: flex; flex-direction: column; align-items: center; justify-content: center; text-align: center; line-height: 1; }
  .discount-badge__value { font-weight: 700; font-size: 34px; }
  .discount-badge__label { font-weight: 700; font-size: 12px; margin-top: 5px; text-transform: uppercase; line-height: 14px; }

  .offer { position: absolute; left: 412px; top: 70px; width: 340px; }
  .offer__title { font-weight: 700; font-size: 31px; color: var(--brand-red); line-height: 1; margin-left: 28px; }
  .offer__tagline { font-weight: 700; font-size: 12.5px; line-height: 19px; text-transform: uppercase; margin: 10px 0 0 29px; }
  .offer__intro { font-size: 15px; margin: 12px 0 0 0; }
  .offer__intro strong { color: var(--brand-red); }

  .package-list { list-style: none; margin: 6px 0 0 17px; font-family: "Tinos", "Times New Roman", serif; font-size: 13.5px; }
  .package-list li { display: flex; align-items: center; height: 19.5px; }
  .package-list svg { width: 14px; height: 14px; margin-right: 6px; flex: none; }

  .offer__cta { margin: 9px 0 0 17px; font-weight: 700; font-size: 15px; color: var(--brand-red); }

  .section-label { position: absolute; left: 22px; background: var(--brand-red); color: var(--paper); font-weight: 700; font-size: 18.5px; line-height: 22px; padding: 0 18px 0 5px; }
  .section-label--about { top: 18px; }
  .section-label--contact { top: 277px; }

  .about { position: absolute; left: 22px; top: 50px; width: 720px; font-size: 14.5px; line-height: 17px; }
  .about p + p { margin-top: 10px; }

  .services { position: absolute; left: 22px; top: 200px; list-style: none; display: flex; gap: 10px; }
  .services li { background: var(--backdrop); font-size: 13px; font-weight: 700; padding: 6px 12px; }

  .contact { position: absolute; left: 24px; top: 312px; list-style: none; font-family: "Tinos", "Times New Roman", serif; }
  .contact li { display: flex; align-items: center; height: 18px; }
  .contact svg { width: 11px; height: 11px; margin-right: 7px; flex: none; }
  .contact__phone { font-weight: 700; font-size: 16px; color: var(--brand-red); }
  .contact__email { font-size: 14px; }
  .contact__web { font-size: 14px; color: var(--brand-red); }

  .back-cta { position: absolute; right: 42px; top: 282px; font-weight: 700; font-size: 17px; color: var(--ink); }

  .footer-band { position: absolute; left: 0; right: 0; bottom: 0; height: 13px; background: var(--brand-red); }
</style>
</head>
<body>

  <section class="postcard postcard--front">
    <svg class="front-art" width="769" height="383" viewBox="0 0 769 383">
      <defs>
        <linearGradient id="photoTone" x1="0" y1="0" x2="1" y2="1">
          <stop offset="0" stop-color="var(--photo-light)"/>
          <stop offset=".55" stop-color="var(--photo-mid)"/>
          <stop offset="1" stop-color="var(--photo-dark)"/>
        </linearGradient>
      </defs>
      <polygon role="img" aria-label="Photo of a smiling team of young professionals, the man in front pointing at the viewer" points="0,0 436,0 284,383 0,383" fill="url(#photoTone)"/>
      <polygon points="436,0 449,0 297,383 284,383" fill="var(--brand-red)"/>
    </svg>

    <div class="discount-badge">
      <span class="discount-badge__value">20% OFF</span>
      <span class="discount-badge__label">Introductory<br>rate</span>
    </div>

    <div class="brand-name">Brightwave HR</div>

    <div class="offer">
      <h1 class="offer__title">Recruitment Special</h1>
      <p class="offer__tagline">People are your best asset, right?…No,<br>the right people are!!!!</p>
      <p class="offer__intro">Our <strong>Recruitment Package</strong> includes<strong>…</strong></p>
      <ul class="package-list">
        <li><svg viewBox="0 0 14 14"><path d="M1 8 L5 12 L13 1" fill="none" stroke="var(--brand-red)" stroke-width="2.2"/></svg>On site review of the role</li>
        <li><svg viewBox="0 0 14 14"><path d="M1 8 L5 12 L13 1" fill="none" stroke="var(--brand-red)" stroke-width="2.2"/></svg>Multi-channel advertising</li>
        <li><svg viewBox="0 0 14 14"><path d="M1 8 L5 12 L13 1" fill="none" stroke="var(--brand-red)" stroke-width="2.2"/></svg>CV screening &amp; phone interviews</li>
        <li><svg viewBox="0 0 14 14"><path d="M1 8 L5 12 L13 1" fill="none" stroke="var(--brand-red)" stroke-width="2.2"/></svg>Face to face interviews</li>
        <li><svg viewBox="0 0 14 14"><path d="M1 8 L5 12 L13 1" fill="none" stroke="var(--brand-red)" stroke-width="2.2"/></svg>Reference checks</li>
        <li><svg viewBox="0 0 14 14"><path d="M1 8 L5 12 L13 1" fill="none" stroke="var(--brand-red)" stroke-width="2.2"/></svg>4 month warranty</li>
        <li><svg viewBox="0 0 14 14"><path d="M1 8 L5 12 L13 1" fill="none" stroke="var(--brand-red)" stroke-width="2.2"/></svg>Flat rate – now 20% off</li>
      </ul>
      <p class="offer__cta">Call 0412 555 018 to book today!</p>
    </div>
  </section>

  <section class="postcard postcard--back">
    <h2 class="section-label section-label--about">About Us:</h2>
    <div class="about">
      <p>We align your people and culture with your business vision, values and strategy – so you can get on with growing your business.</p>
      <p>Sam Harlow (Principal) brings 20+ years in national sales, key accounts and training, plus 5 years as General Manager HR building HR systems from the ground up.</p>
      <p>Personable, professional and practical HR for small to medium businesses.</p>
    </div>
    <ul class="services">
      <li>Recruitment</li>
      <li>HR Systems</li>
      <li>People &amp; Culture</li>
      <li>Training</li>
    </ul>

    <h2 class="section-label section-label--contact">Contact Us:</h2>
    <ul class="contact">
      <li class="contact__phone"><svg viewBox="0 0 12 12"><path d="M3 1 L5 3.5 L3.8 5 Q5 7.5 7 8.2 L8.5 7 L11 9 L9.5 11 Q4 10.5 1 3 Z" fill="none" stroke="var(--ink)" stroke-width="1"/></svg>0412 555 018</li>
      <li class="contact__email"><svg viewBox="0 0 12 12"><rect x="1" y="2.5" width="10" height="7" fill="none" stroke="var(--ink)" stroke-width="1"/><path d="M1 2.5 L6 7 L11 2.5" fill="none" stroke="var(--ink)" stroke-width="1"/></svg>sharlow@brightwavehr.com.au</li>
      <li class="contact__web"><svg viewBox="0 0 12 12"><path d="M3 1 L3 9 L5 7.3 L6.5 11 L8 10.3 L6.6 6.8 L9.3 6.6 Z" fill="none" stroke="var(--ink)" stroke-width="1"/></svg>www.brightwavehr.com.au</li>
    </ul>

    <p class="back-cta">Book your free HR chat today!</p>
    <div class="brand-name">Brightwave HR</div>
    <div class="footer-band"></div>
  </section>

</body>
</html>
```